Eye-catching Card for new church

I would like a card the size of a business card ... that can be used to announce the start of our new church. I would like it to have our logo on the card, my name, and the statement "Coming Soon ... 1.10.2016". I also would like to list our website address and Facebook page and my Twitter account.

Target Market(s)

prospective people looking for a church

Industry/Entity Type

Church

Requirements
Must have
• a focus on Coming Soon ... 1.10.2016
• Brightfold Church logo
Should not have
• church buildings or writings on the cross

```html
<!DOCTYPE html>
<html lang="en">
<head>
<meta charset="utf-8">
<title>Brightfold Church – Coming Soon Card</title>
<link href="https://fonts.googleapis.com/css2?family=Open+Sans:wght@400;600;700&display=swap" rel="stylesheet">
<style>
  :root {
    --backdrop: #2b2b2b;
    --card-white: #ffffff;
    --card-blue: #1569b3;
    --ink-dark: #454545;
    --ink-body: #333333;
    --accent-blue: #1a6cb5;
    --icon-blue: #2a86d0;
    --mark-faint: #e6e6e8;
  }
  * { margin: 0; padding: 0; box-sizing: border-box; }
  html, body {
    width: 1200px; height: 900px; overflow: hidden;
    background: var(--backdrop);
    font-family: "Open Sans", Arial, sans-serif;
  }
  .canvas { position: relative; width: 1200px; height: 900px; }

  .card { position: absolute; border-radius: 18px; overflow: hidden; }
  .card--front {
    left: 332px; top: 125px; width: 546px; height: 316px;
    background: var(--card-white);
  }
  .card--back {
    left: 330px; top: 506px; width: 557px; height: 322px;
    background: var(--card-blue);
  }

  .brand-lockup { position: absolute; display: flex; align-items: center; }
  .brand-dot { flex: none; border-radius: 50%; }
  .brand-name {
    font-weight: 600; text-transform: uppercase;
    text-align: center; line-height: 1.15;
  }
  .brand-name .brand-sub { display: block; }

  .card--front .brand-lockup { left: 30px; top: 112px; gap: 12px; }
  .card--front .brand-dot { width: 22px; height: 22px; background: var(--accent-blue); }
  .card--front .brand-name { color: var(--ink-dark); font-size: 19px; letter-spacing: 3px; }
  .card--front .brand-sub { font-size: 10px; letter-spacing: 6px; }

  .card--back .brand-lockup {
    left: 0; top: 0; width: 100%; height: 100%;
    justify-content: center; gap: 20px;
  }
  .card--back .brand-dot { width: 40px; height: 40px; background: var(--card-white); }
  .card--back .brand-name { color: var(--card-white); font-size: 30px; letter-spacing: 5px; }
  .card--back .brand-sub { font-size: 15px; letter-spacing: 12px; margin-top: 4px; }

  .announcer {
    position: absolute; right: 35px; top: 141px; text-align: right;
  }
  .announcer-name { color: var(--ink-dark); font-size: 21px; font-weight: 700; line-height: 1.2; }
  .announcer-date { color: var(--accent-blue); font-size: 15px; line-height: 1.3; }

  .contact-list {
    position: absolute; left: 26px; top: 206px; list-style: none;
  }
  .contact-item {
    display: flex; align-items: center; height: 23px;
    color: var(--ink-body); font-size: 15px;
  }
  .contact-icon { width: 12px; height: 12px; margin-right: 19px; flex: none; }
</style>
</head>
<body>
<main class="canvas">
  <section class="card card--front" aria-label="Card front">
    <div class="brand-lockup">
      <span class="brand-dot"></span>
      <div class="brand-name">Brightfold<span class="brand-sub">Church</span></div>
    </div>

    <div class="announcer">
      <p class="announcer-name">Alan Reeve</p>
      <p class="announcer-date">Coming Soon ... 1.10.2016</p>
    </div>

    <ul class="contact-list">
      <li class="contact-item">
        <svg class="contact-icon" viewBox="0 0 12 12"><circle cx="6" cy="6" r="4" fill="var(--icon-blue)"/></svg>
        Brightfold.page/yourname
      </li>
      <li class="contact-item">
        <svg class="contact-icon" viewBox="0 0 12 12"><circle cx="6" cy="6" r="4" fill="var(--icon-blue)"/></svg>
        @yourname
      </li>
      <li class="contact-item">
        <svg class="contact-icon" viewBox="0 0 12 12" fill="none" stroke="var(--icon-blue)" stroke-width="1.6" stroke-linecap="round">
          <path d="M5 7 L7 5"/>
          <path d="M4.2 5.6 L2.8 7 a2 2 0 0 0 2.8 2.8 L7 8.4"/>
          <path d="M7.8 6.4 L9.2 5 a2 2 0 0 0 -2.8 -2.8 L5 3.6"/>
        </svg>
        www.website.com
      </li>
    </ul>
  </section>

  <section class="card card--back" aria-label="Card back">
    <div class="brand-lockup">
      <span class="brand-dot"></span>
      <div class="brand-name">Brightfold<span class="brand-sub">Church</span></div>
    </div>
  </section>
</main>
</body>
</html>
```